BrimFalcon Business Cards

We have a defined brand. Please visit our website to get a feel for the product and the color pallets. www.brimfalcon-demo.com

We need an updated, world class business card design. (See the attached existing card design). Please utilize BOTH sides of the card as shown and be creative with the layout. I do want the horse head icon to be positioned as it is with the existing card.

The remainder of the layout can be customized and I also want it vertically oriented.

Attached are the logo files and please use the colors as follows:
Green - #A5CE39
Tan - #CDBD99
Black

Feel free to play with the colors.

```html
<!DOCTYPE html>
<html lang="en">
<head>
<meta charset="UTF-8">
<title>BrimFalcon Labs – Business Card</title>
<link href="https://fonts.googleapis.com/css2?family=Poppins:wght@300;400;500&display=swap" rel="stylesheet">
<style>
  :root {
    --backdrop: #b9b9bb;
    --card-black: #141414;
    --card-black-soft: #1f1f1f;
    --brand-green: #a5ce39;
    --green-light: #9fd03f;
    --green-deep: #2f8a3e;
    --text-white: #f2f2f2;
    --ink: #111111;
  }
  * { box-sizing: border-box; margin: 0; padding: 0; }
  html, body { width: 1200px; height: 876px; overflow: hidden; }
  body {
    background: var(--backdrop);
    font-family: "Poppins", sans-serif;
    position: relative;
  }
  .card {
    position: absolute;
    top: 60px;
    width: 430px;
    height: 756px;
    border-radius: 18px;
    overflow: hidden;
    box-shadow: 0 14px 30px rgba(0,0,0,0.28);
  }
  /* Front: contact side */
  .card-front {
    left: 130px;
    background: var(--card-black);
  }
  .front-emblem {
    position: absolute;
    left: 40px;
    top: 70px;
    width: 340px;
    height: 360px;
    border-radius: 50%;
    background: radial-gradient(circle at 55% 45%, var(--card-black-soft) 0%, #181818 55%, var(--card-black) 75%);
  }
  .contact-block {
    position: absolute;
    left: 0;
    right: 0;
    top: 420px;
    text-align: center;
  }
  .person-name {
    color: var(--brand-green);
    font-weight: 500;
    font-size: 46px;
    line-height: 1.05;
  }
  .person-title {
    color: var(--text-white);
    font-weight: 300;
    font-size: 24px;
    margin-top: 4px;
  }
  .contact-list {
    list-style: none;
    margin: 22px auto 0;
    width: 270px;
    text-align: left;
  }
  .contact-list li {
    display: flex;
    align-items: center;
    gap: 12px;
    color: var(--text-white);
    font-weight: 300;
    font-size: 19px;
    line-height: 1.55;
    white-space: nowrap;
  }
  .contact-list svg { width: 17px; height: 17px; flex: none; }
  .location {
    position: absolute;
    left: 0;
    right: 0;
    bottom: 44px;
    display: flex;
    justify-content: center;
    align-items: center;
    gap: 10px;
    color: var(--brand-green);
    font-weight: 300;
    font-size: 20px;
  }
  .location svg { width: 16px; height: 22px; }
  /* Back: brand side */
  .card-back {
    left: 640px;
    background: linear-gradient(160deg, var(--green-light) 0%, #7fbe42 45%, var(--green-deep) 100%);
  }
  .back-emblem {
    position: absolute;
    left: -40px;
    top: 20px;
    width: 420px;
    height: 460px;
    border-radius: 50%;
    background: radial-gradient(circle at 45% 45%, rgba(47,138,62,0.55) 0%, rgba(80,160,70,0.35) 50%, rgba(165,206,57,0) 72%);
  }
  .brand-mark {
    position: absolute;
    right: 34px;
    bottom: 40px;
    display: flex;
    align-items: center;
    gap: 12px;
    transform-origin: right bottom;
    transform: rotate(-90deg) translateX(100%);
  }
  .brand-dot {
    width: 34px;
    height: 34px;
    border-radius: 50%;
    background: var(--ink);
  }
  .brand-name {
    color: var(--ink);
    font-weight: 500;
    font-size: 40px;
    letter-spacing: 0.5px;
    white-space: nowrap;
  }
</style>
</head>
<body>
  <section class="card card-front">
    <div class="front-emblem" role="img" aria-label="Faint brand emblem illustration in dark tones"></div>
    <div class="contact-block">
      <h1 class="person-name">Dale Remick</h1>
      <p class="person-title">President &amp; CEO</p>
      <ul class="contact-list">
        <li>
          <svg viewBox="0 0 24 24"><path fill="#a5ce39" d="M6.6 10.8a15 15 0 0 0 6.6 6.6l2.2-2.2a1 1 0 0 1 1-.25 11.4 11.4 0 0 0 3.6.57 1 1 0 0 1 1 1V20a1 1 0 0 1-1 1A17 17 0 0 1 3 4a1 1 0 0 1 1-1h3.5a1 1 0 0 1 1 1c0 1.25.2 2.45.57 3.6a1 1 0 0 1-.25 1z"/></svg>
          555.014.2290
        </li>
        <li>
          <svg viewBox="0 0 24 24"><path fill="#a5ce39" d="M2 5h20v14H2z"/><path fill="none" stroke="#141414" stroke-width="2" d="M2 5l10 8 10-8"/></svg>
          BrimFalconLabs.com
        </li>
        <li>
          <svg viewBox="0 0 24 24"><path fill="#a5ce39" d="M2 5h20v14H2z"/><path fill="none" stroke="#141414" stroke-width="2" d="M2 5l10 8 10-8"/></svg>
          Dale@BrimFalcon.com
        </li>
      </ul>
    </div>
    <p class="location">
      <svg viewBox="0 0 16 22"><path fill="#a5ce39" d="M8 0a8 8 0 0 0-8 8c0 6 8 14 8 14s8-8 8-14a8 8 0 0 0-8-8zm0 11a3 3 0 1 1 0-6 3 3 0 0 1 0 6z"/></svg>
      Northfield, Prairie Canada
    </p>
  </section>

  <section class="card card-back">
    <div class="back-emblem" role="img" aria-label="Large brand emblem illustration in deep green tones"></div>
    <div class="brand-mark">
      <span class="brand-dot"></span>
      <span class="brand-name">BrimFalcon Labs</span>
    </div>
  </section>
</body>
</html>
```